Kitchen Tools Infographic - Helpful Items for Healthy Home Meals

We are a weight loss company that provides holistic, natural nutrition programs to consumers -- you can see our web site at www.FernaluVita.com. We need a simple infographic to be shared on social media and via email. The topic for the infographic is "Equip Your Kitchen for Healthy Home Meals". We've outlined 5 groups of kitchen tools that are helpful for consumers to have for preparing home meals, and included some framing statistics emphasizing the weight management benefits of preparing meals versus eating out.

Target Market(s)

Women age 35-55

Industry/Entity Type

Health And Wellness

Font styles to use
Sans Serif

Colors
0292cd
9bcb3b

Requirements
Must have
• - FernaluVita Logo
• - Graphics summarizing statistic (weight gain)
• - Graphics showing groupings of kitchen tools
Should not have
• body scale graphics
• before/after graphics

```html
<!DOCTYPE html>
<html lang="en">
<head>
<meta charset="utf-8">
<title>Equip Your Kitchen for Healthy Home Meals – FernaluVita</title>
<link rel="stylesheet" href="https://fonts.googleapis.com/css2?family=Oswald:wght@300;400;500&family=Lato:wght@400;700&display=swap">
<style>
:root{
  --sky:#2ea3d9;
  --sky-light:#7cc8ec;
  --purple:#7a5aa8;
  --teal:#45bec4;
  --ribbon:#1c8fc9;
  --ribbon-dark:#136e9c;
  --paper:#f1f2f4;
  --salmon:#ef8570;
  --bar-week:#f0676e;
  --bar-meal:#9bcb3b;
  --ink:#222;
  --axis:#333;
  --prep:#e8525a;
  --tech:#8cc63e;
  --cook:#3fb8c0;
  --serve:#ef6f5c;
  --store:#6c5aa6;
  --white:#fff;
}
*{margin:0;padding:0;box-sizing:border-box}
html,body{width:1200px;height:3169px;overflow:hidden;background:var(--paper)}
body{position:relative;font-family:"Lato",sans-serif;color:var(--ink)}
.abs{position:absolute}

/* header */
.masthead{left:0;top:0;width:1200px;height:376px;background:var(--sky)}
.masthead-frame{left:36px;top:24px;width:1128px;height:190px;border:3px solid var(--white);border-bottom:none}
.brand{left:0;top:36px;width:1200px;text-align:center;color:var(--white);font-weight:700;font-size:104px;letter-spacing:4px;line-height:130px}
.title-band{left:76px;top:222px;width:1048px;height:116px;background:var(--purple);display:flex;align-items:center;justify-content:center;border-bottom:4px dotted var(--white)}
.title-band h1{color:var(--white);font-family:"Oswald",sans-serif;font-weight:400;font-size:50px;letter-spacing:1px}

/* why cook */
.why{left:0;top:376px;width:1200px;height:226px;background:var(--teal);color:var(--white);text-align:center}
.why h2{font-family:"Oswald",sans-serif;font-weight:300;font-size:34px;margin-top:36px;display:inline-block;padding:0 24px;border-bottom:3px dotted var(--white)}
.why p{font-size:22px;line-height:32px;padding:24px 48px 0}

/* ribbons */
.ribbon{height:74px;background:var(--ribbon);color:var(--white);display:flex;align-items:center;justify-content:center}
.ribbon span{font-family:"Oswald",sans-serif;font-size:32px;border:3px dashed var(--white);padding:4px 16px}
.ribbon-end{width:60px;height:74px;background:var(--ribbon-dark)}

/* bar chart */
.bar-label{font-size:27px;left:20px}
.bar{height:24px}
.tick{font-size:27px;width:80px;text-align:center}

/* line chart */
.gain{left:0;top:1099px;width:1200px;height:545px}
.pill{left:268px;top:41px;width:664px;height:54px;background:var(--white);border-radius:27px;color:var(--salmon);display:flex;align-items:center;justify-content:center;font-family:"Oswald",sans-serif;font-size:30px}

/* tools */
.group{left:86px;width:1080px}
.group-icon{width:68px;height:68px;left:-4px;top:-16px}
.group-title{left:104px;top:0;font-family:"Oswald",sans-serif;font-size:30px;line-height:36px}
.tool{left:104px;font-size:22px;line-height:30px;white-space:nowrap}
.tool b{font-weight:700}

/* call band */
.cta{left:30px;top:2658px;width:1140px;height:110px;background:var(--ribbon);color:var(--white)}
.cta p{position:absolute;font-size:26px;font-weight:700;line-height:32px}
.cta-icon{width:54px;height:50px;background:var(--white);opacity:0.9;border-radius:6px}

/* sources */
.sources{left:144px;top:2747px;width:912px;height:253px;background:var(--purple);color:var(--white);text-align:center}
.sources h2{font-family:"Oswald",sans-serif;font-weight:400;font-size:52px;margin-top:52px}
.sources p{font-size:19px;line-height:38px}

.stripe-band{left:0;top:3026px;width:1200px;height:22px;background:var(--sky-light)}
.footer{left:0;top:3064px;width:1200px;height:105px;background:var(--sky);color:var(--white);text-align:center;font-size:42px;line-height:105px}
</style>
</head>
<body>

<header class="abs masthead">
  <div class="abs masthead-frame"></div>
  <div class="abs brand">FERNALUVITA</div>
  <div class="abs title-band"><h1>EQUIP YOUR KITCHEN FOR HEALTHY HOME MEALS</h1></div>
</header>

<section class="abs why">
  <h2>WHY COOK AT HOME</h2>
  <p>Those who eat out consume an average of 134 calories more per meal. Americans eat out an average of 4.5 times per week, so those extra calories can add up to substantial weight gain – and give you a reason to prepare your own meals.</p>
</section>

<section class="excess">
  <div class="abs ribbon-end" style="left:140px;top:646px"></div>
  <div class="abs ribbon-end" style="left:1000px;top:646px"></div>
  <div class="abs ribbon" style="left:180px;top:634px;width:840px"><span>EXCESS CALORIES FROM RESTAURANT MEALS</span></div>

  <svg class="abs" style="left:0;top:740px" width="1200" height="310" aria-hidden="true">
    <line x1="290" y1="20" x2="290" y2="295" stroke="var(--axis)" stroke-width="2"/>
    <line x1="290" y1="295" x2="1152" y2="295" stroke="var(--axis)" stroke-width="2"/>
  </svg>
  <div class="abs" role="img" aria-label="Small running figure icon" style="left:300px;top:862px;width:46px;height:46px;background:var(--purple);border-radius:8px"></div>
  <div class="abs bar-label" style="top:909px;color:var(--bar-week)">Calories Per Week</div>
  <div class="abs bar" style="left:290px;top:915px;width:738px;background:var(--bar-week)"></div>
  <div class="abs bar-label" style="top:979px;color:var(--bar-meal)">Calories Per Meal</div>
  <div class="abs bar" style="left:290px;top:983px;width:165px;background:var(--bar-meal)"></div>
  <div class="abs tick" style="left:250px;top:1045px">0</div>
  <div class="abs tick" style="left:373px;top:1045px">100</div>
  <div class="abs tick" style="left:496px;top:1045px">200</div>
  <div class="abs tick" style="left:619px;top:1045px">300</div>
  <div class="abs tick" style="left:742px;top:1045px">400</div>
  <div class="abs tick" style="left:865px;top:1045px">500</div>
  <div class="abs tick" style="left:988px;top:1045px">600</div>
  <div class="abs tick" style="left:1112px;top:1045px">700</div>
</section>

<section class="abs gain">
  <svg class="abs" style="left:0;top:0" width="1200" height="545" role="img" aria-label="Line chart: about 1.5 lb gained after 2 months, 4.5 lb after 4 months, 9 lb after 6 months">
    <rect width="1200" height="530" fill="var(--salmon)"/>
    <polyline fill="var(--salmon)" points="0,530 15,545 30,530 45,545 60,530 75,545 90,530 105,545 120,530 135,545 150,530 165,545 180,530 195,545 210,530 225,545 240,530 255,545 270,530 285,545 300,530 315,545 330,530 345,545 360,530 375,545 390,530 405,545 420,530 435,545 450,530 465,545 480,530 495,545 510,530 525,545 540,530 555,545 570,530 585,545 600,530 615,545 630,530 645,545 660,530 675,545 690,530 705,545 720,530 735,545 750,530 765,545 780,530 795,545 810,530 825,545 840,530 855,545 870,530 885,545 900,530 915,545 930,530 945,545 960,530 975,545 990,530 1005,545 1020,530 1035,545 1050,530 1065,545 1080,530 1095,545 1110,530 1125,545 1140,530 1155,545 1170,530 1185,545 1200,530"/>
    <line x1="120" y1="68" x2="1080" y2="68" stroke="#fff" stroke-width="3" stroke-dasharray="10 8"/>
    <g stroke="#fff" stroke-opacity="0.55" stroke-width="1.5" stroke-dasharray="6 5">
      <line x1="184" y1="154" x2="1060" y2="154"/>
      <line x1="184" y1="213" x2="1060" y2="213"/>
      <line x1="184" y1="272" x2="1060" y2="272"/>
      <line x1="184" y1="332" x2="1060" y2="332"/>
      <line x1="184" y1="391" x2="1060" y2="391"/>
    </g>
    <line x1="184" y1="450" x2="1060" y2="450" stroke="#fff" stroke-width="2"/>
    <polyline fill="none" stroke="#fff" stroke-width="4" points="184,450 334,406 636,317 938,184"/>
    <g fill="#fff">
      <circle cx="334" cy="406" r="11"/>
      <circle cx="636" cy="317" r="11"/>
      <circle cx="938" cy="184" r="11"/>
    </g>
    <g fill="#fff" font-family="Lato, sans-serif" font-size="30" text-anchor="end">
      <text x="150" y="164">10</text>
      <text x="150" y="223">8</text>
      <text x="150" y="282">6</text>
      <text x="150" y="342">4</text>
      <text x="150" y="401">2</text>
      <text x="150" y="460">0</text>
    </g>
    <g fill="#fff" font-family="Lato, sans-serif" font-size="30" text-anchor="middle">
      <text x="334" y="490">2 months</text>
      <text x="636" y="490">4 months</text>
      <text x="938" y="490">6 months</text>
    </g>
  </svg>
  <div class="abs pill">POUNDS GAINED FROM RESTAURANT MEALS</div>
</section>

<section class="tools">
  <div class="abs ribbon-end" style="left:86px;top:1688px"></div>
  <div class="abs ribbon-end" style="left:1054px;top:1688px"></div>
  <div class="abs ribbon" style="left:126px;top:1676px;width:948px"><span>MAKE HEALTHY EATING EASIER WITH THESE KITCHEN TOOLS</span></div>

  <div class="abs group" style="top:1803px">
    <svg class="abs group-icon" viewBox="0 0 68 68" aria-hidden="true"><circle cx="34" cy="34" r="31" fill="none" stroke="var(--prep)" stroke-width="3"/><circle cx="34" cy="34" r="20" fill="var(--prep)"/><line x1="26" y1="42" x2="42" y2="26" stroke="#fff" stroke-width="4" stroke-linecap="round"/></svg>
    <div class="abs group-title" style="color:var(--prep)">PREP</div>
    <div class="abs tool" style="top:48px"><b>Cutting Board</b>–essential for prepping meat and vegetables.</div>
    <div class="abs tool" style="top:84px"><b>Chef's Knife</b>–go for quality to make chopping, dicing and slicing faster and easier.</div>
    <div class="abs tool" style="top:120px"><b>Digital Food Scale</b>– get the precision you need for perfect recipes and portion control.</div>
  </div>

  <div class="abs group" style="top:1972px">
    <svg class="abs group-icon" viewBox="0 0 68 68" aria-hidden="true"><circle cx="34" cy="34" r="31" fill="none" stroke="var(--tech)" stroke-width="3"/><circle cx="34" cy="34" r="20" fill="var(--tech)"/><rect x="25" y="30" width="18" height="12" rx="2" fill="#fff"/></svg>
    <div class="abs group-title" style="color:var(--tech)">TECH</div>
    <div class="abs tool" style="top:46px"><b>High-Powered Blender</b>–make highly nutritious, healthy drinks from fruits and veggies</div>
    <div class="abs tool" style="top:82px"><b>Slow Cooker</b>- cook delicious meals while you are at work</div>
    <div class="abs tool" style="top:118px"><b>Pressure Cooker</b>-create single pot meals in 20 minutes or less</div>
  </div>

  <div class="abs group" style="top:2141px">
    <svg class="abs group-icon" viewBox="0 0 68 68" aria-hidden="true"><circle cx="34" cy="34" r="31" fill="none" stroke="var(--cook)" stroke-width="3"/><circle cx="34" cy="34" r="20" fill="var(--cook)"/><circle cx="34" cy="36" r="7" fill="#fff"/></svg>
    <div class="abs group-title" style="color:var(--cook)">COOK</div>
    <div class="abs tool" style="top:46px"><b>Ceramic Pan</b>–nonstick cooking surface allows you to cook without oil</div>
    <div class="abs tool" style="top:82px"><b>Vegetable Steamer</b>– preserve nutrients and natural, fresh taste</div>
    <div class="abs tool" style="top:118px"><b>Baking Sheet</b>–ideal for roasting vegetables in the oven or baking chicken and fish <b>dishes</b></div>
  </div>

  <div class="abs group" style="top:2310px">
    <svg class="abs group-icon" viewBox="0 0 68 68" aria-hidden="true"><circle cx="34" cy="34" r="31" fill="none" stroke="var(--serve)" stroke-width="3"/><circle cx="34" cy="34" r="20" fill="var(--serve)"/><path d="M23 40 A11 11 0 0 1 45 40 Z" fill="#fff"/></svg>
    <div class="abs group-title" style="color:var(--serve)">SERVE</div>
    <div class="abs tool" style="top:46px"><b>Cloth Napkins</b> – to reduce waste and dress up your table</div>
    <div class="abs tool" style="top:82px"><b>Dinnerware</b>– pre-plate meals rather than serving family style to control portions</div>
    <div class="abs tool" style="top:118px"><b>Small Plates</b> – use salad plates and smaller dishware to manage perception of food <b>volume</b></div>
  </div>

  <div class="abs group" style="top:2480px">
    <svg class="abs group-icon" viewBox="0 0 68 68" aria-hidden="true"><circle cx="34" cy="34" r="31" fill="none" stroke="var(--store)" stroke-width="3"/><circle cx="34" cy="34" r="20" fill="var(--store)"/><rect x="26" y="24" width="16" height="20" rx="2" fill="#fff"/><line x1="26" y1="34" x2="42" y2="34" stroke="var(--store)" stroke-width="2"/></svg>
    <div class="abs group-title" style="color:var(--store)">STORE</div>
    <div class="abs tool" style="top:46px"><b>Glass Storage Containers</b>–keep your healthy leftovers so nothing goes to waste</div>
    <div class="abs tool" style="top:82px"><b>Mason Jars</b> – perfect for premade salads that you can bring to work</div>
    <div class="abs tool" style="top:118px"><b>Freezer Safe Re-</b> Sealable Bags –prepare double batches to make the most of your <b>time</b></div>
  </div>
</section>

<section class="abs cta">
  <div class="abs cta-icon" role="img" aria-label="Handshake icon" style="left:28px;top:30px"></div>
  <p style="left:108px;top:22px">FernaluVita can help you develop<br>healthier eating habits.</p>
  <div class="abs cta-icon" role="img" aria-label="Two people meeting icon" style="left:660px;top:30px;width:70px"></div>
  <p style="left:752px;top:38px">We invite you to learn more.</p>
</section>
<svg class="abs" style="left:30px;top:2768px" width="1140" height="60" aria-hidden="true">
  <polygon points="0,0 114,0 114,56" fill="var(--ribbon-dark)"/>
  <polygon points="1140,0 1026,0 1026,56" fill="var(--ribbon-dark)"/>
</svg>

<section class="abs sources">
  <h2>— SOURCES —</h2>
  <p style="margin-top:22px">www.harvestdata.org/field-notes/2010/june/eating-out-increases-daily-calorie-intake/</p>
  <p>www.tablepulse.com/b/the-state-of-american-dining-in-2016</p>
</section>

<div class="abs stripe-band" role="img" aria-label="Decorative stripe band in light blue"></div>

<footer class="abs footer">www.FernaluVita.com</footer>

</body>
</html>
```